Launderette Window Advertising

We are opening a new launderette / laundromat in the UK and want to create some designs for our shop windows. There are 5 large windows in total and 2 entry doors which we would like to create advertising for.

Pictures attached.

the 3 windows on the right will be covered up completely with writing and pictures relating to the shops activities also 1 window right of the doors.

of the 2 entry doors the door on the left will have the company logo, opening times and social media.

Opening Times
Monday - Friday 9am - 6pm
Saturday & Sunday 9am - 7pm

Social Media
Instagram BrookvaleLaneLaundry
Facebook Brookvale Lane Laundry

window on the left of the door will have a display window where we will display our services and costs.

On the bigger windows display our services such as

Serviced Laundry - Wash, Dry, Iron & Fold

Self Service Wash & Dry

Ironing Service

B&B, Stayvio and Hotel customers.
Free pickup & Delivery. T&C's Apply.

Target Market(s)

mainly women 20+

Industry/Entity Type

Laundry

Font styles to use
Serif
Sans Serif

Colors
0054AA
0677BA
7BADD7
CADEEF
E8F1F8
0094D4
00A9DD
6FCCEA
C7EBF8
E9F6FB
59FF00
82FF00
B8FF75
E3FFCB
F4FFEA

Requirements
Must have
• Minimalistic designs ,easy to read

```html
<!DOCTYPE html>
<html lang="en">
<head>
<meta charset="utf-8">
<title>Brookvale Lane Laundry – Window &amp; Door Graphics</title>
<link href="https://fonts.googleapis.com/css2?family=Figtree:wght@400;500;600;700&display=swap" rel="stylesheet">
<style>
  :root {
    --brand-blue: #0094D4;
    --pale-blue: #E8F1F8;
    --white: #FFFFFF;
  }
  * { box-sizing: border-box; margin: 0; padding: 0; }
  html, body { width: 1200px; height: 690px; overflow: hidden; background: var(--white); }
  body { position: relative; font-family: "Figtree", "Helvetica Neue", Arial, sans-serif; }

  .section-bar {
    position: absolute; left: 0; top: 34px; width: 1200px; height: 32px;
    background: var(--brand-blue);
  }
  .section-label {
    position: absolute; top: 0; line-height: 32px;
    color: var(--white); font-weight: 600; font-size: 21px; letter-spacing: 0.3px;
    transform: translateX(-50%);
  }
  .section-label--window { left: 283px; }
  .section-label--doors { left: 878px; }

  /* Window 1 */
  .window-panel {
    position: absolute; left: 45px; top: 83px; width: 504px; height: 572px;
    background: var(--brand-blue);
  }
  .price-board {
    position: absolute; left: 90px; top: 150px; width: 322px; height: 273px;
    border: 4px solid var(--pale-blue); background: var(--brand-blue);
  }
  .price-list {
    position: absolute; left: 0; top: 0; right: 0; height: 199px;
    padding: 18px 24px 0 18px; color: var(--white);
  }
  .service { margin-bottom: 13px; }
  .service-title { font-weight: 700; font-size: 14.5px; line-height: 20px; }
  .service-detail { font-weight: 400; font-size: 14.5px; line-height: 20px; }
  .price-row { display: flex; align-items: flex-end; }
  .leader {
    flex: 1; height: 4px; margin: 0 6px 4px 7px;
    background-image: radial-gradient(circle, var(--white) 1.1px, transparent 1.4px);
    background-size: 7.2px 4px; background-repeat: repeat-x;
  }
  .price { font-weight: 700; }
  .offer-band {
    position: absolute; left: 0; right: 0; top: 199px; height: 59px;
    background: var(--pale-blue); color: var(--brand-blue);
    font-weight: 600; font-size: 14px; line-height: 21px; padding: 10px 0 0 18px; letter-spacing: 0.15px;
  }
  .offer-rule {
    position: absolute; left: 0; right: 0; top: 258px; height: 7px; background: var(--brand-blue);
  }

  /* Doors */
  .door { position: absolute; top: 84px; width: 253px; height: 575px; overflow: hidden; }
  .door--name { left: 616px; background: var(--pale-blue); }
  .door-wordmark {
    position: absolute; left: 6px; bottom: -6px;
    color: var(--brand-blue); font-weight: 700; font-size: 74px; line-height: 66px;
    white-space: nowrap; letter-spacing: -1px;
  }
  .door-wordmark span { display: block; }
  .door-wordmark span + span { padding-left: 112px; }

  .door--info { left: 882px; background: var(--brand-blue); }
  .door-frame {
    position: absolute; left: 12px; top: 14px; width: 229px; height: 547px;
    border: 4px solid var(--pale-blue);
  }
  .logo-area { position: absolute; left: 0; top: 0; right: 0; height: 230px; }
  .logo-ring {
    position: absolute; left: 40px; top: 41px; width: 150px; height: 150px;
    border: 3px solid var(--white); border-radius: 50%;
  }
  .logo-name {
    position: absolute; left: 0; right: 0; top: 92px; text-align: center;
    color: var(--white); font-weight: 700; font-size: 23px; line-height: 26px;
  }
  .info-band {
    position: absolute; left: 0; right: 0; top: 230px; height: 101px;
    background: var(--pale-blue); color: var(--brand-blue); text-align: center;
    font-weight: 600; font-size: 9.2px; letter-spacing: 0.6px;
  }
  .hours { padding-top: 14px; line-height: 11.7px; }
  .social-dot {
    display: block; width: 14px; height: 14px; border-radius: 50%;
    background: var(--brand-blue); margin: 11px auto 0;
  }
  .handle { margin-top: 8px; font-size: 10.5px; letter-spacing: 0.8px; }
</style>
</head>
<body>
  <header class="section-bar">
    <h2 class="section-label section-label--window">WINDOW 1</h2>
    <h2 class="section-label section-label--doors">DOORS</h2>
  </header>

  <section class="window-panel">
    <div class="price-board">
      <div class="price-list">
        <div class="service">
          <p class="service-title">SERVICED LAUNDRY</p>
          <p class="service-detail">WASH, DRY,</p>
          <p class="service-detail price-row">IRON &amp; FOLD <span class="leader"></span><span class="price">0.00</span></p>
        </div>
        <div class="service">
          <p class="service-title">SELF SERVICE</p>
          <p class="service-detail price-row">WASH &amp; DRY <span class="leader"></span><span class="price">0.00</span></p>
        </div>
        <div class="service">
          <p class="service-title price-row">IRONING SERVICE<span class="leader"></span><span class="price">0.00</span></p>
        </div>
      </div>
      <p class="offer-band">B&amp;B, STAYVIO AND HOTEL CUSTOMERS<br>FREE PICKUP &amp; DELIVERY. T&amp;C'S APPLY.</p>
      <div class="offer-rule"></div>
    </div>
  </section>

  <section class="door door--name">
    <p class="door-wordmark"><span>Brookvale</span><span>Lane</span></p>
  </section>

  <section class="door door--info">
    <div class="door-frame">
      <div class="logo-area">
        <div class="logo-ring"></div>
        <p class="logo-name">Brookvale<br>Lane</p>
      </div>
      <div class="info-band">
        <p class="hours">OPENING TIMES<br>MONDAY - FRIDAY 9AM - 6PM<br>SATURDAY &amp; SUNDAY 9AM - 7PM</p>
        <span class="social-dot"></span>
        <p class="handle">BROOKVALELANE LAUNDRY</p>
      </div>
    </div>
  </section>
</body>
</html>
```